PL Dunmore Electric Yard Sign

Looking to have a yard sign designed that we can place at projects we are working on. Most likely will be 18" H x 24" W but flexible that we can increase the size if necessary. It should include our logo, our phone # 555-214-7796, website pldunmoreelectric.example and slogan, built on integrity, driven by excellence. Colors should match our brand.

```html
<!DOCTYPE html>
<html lang="en">
<head>
<meta charset="utf-8">
<title>PL Dunmore Electric Yard Sign</title>
<link rel="stylesheet" href="https://fonts.googleapis.com/css2?family=Poppins:wght@500;600;700&family=Montserrat:wght@500&display=swap">
<style>
  :root {
    --navy: #16335f;
    --red: #e9222b;
    --white: #ffffff;
  }
  html, body {
    margin: 0;
    padding: 0;
    width: 1200px;
    height: 877px;
    overflow: hidden;
    background: var(--white);
  }
  .yard-sign {
    position: relative;
    width: 1200px;
    height: 877px;
    background: var(--white);
  }
  .brand {
    position: absolute;
    left: 0;
    top: 0;
    width: 1200px;
    height: 462px;
    display: flex;
    align-items: center;
    justify-content: center;
    gap: 28px;
  }
  .brand-dot {
    width: 46px;
    height: 46px;
    border-radius: 50%;
    background: var(--red);
    flex: none;
  }
  .brand-name {
    margin: 0;
    font-family: "Poppins", sans-serif;
    font-weight: 600;
    font-size: 78px;
    letter-spacing: 1px;
    color: var(--navy);
  }
  .slogan-band {
    position: absolute;
    left: 0;
    top: 462px;
    width: 1200px;
    height: 98px;
    background: var(--navy);
    display: flex;
    align-items: center;
    justify-content: center;
  }
  .slogan {
    margin: 0;
    font-family: "Poppins", sans-serif;
    font-weight: 600;
    font-size: 41px;
    color: var(--white);
  }
  .phone-band {
    position: absolute;
    left: 0;
    top: 560px;
    width: 1200px;
    height: 207px;
    background: var(--red);
    display: flex;
    align-items: center;
    justify-content: center;
  }
  .phone {
    margin: 0;
    font-family: "Poppins", sans-serif;
    font-weight: 700;
    font-size: 124px;
    line-height: 1;
    padding-top: 10px;
    color: var(--white);
  }
  .rule {
    position: absolute;
    left: 0;
    top: 767px;
    width: 1200px;
    height: 18px;
    background: var(--navy);
  }
  .website {
    position: absolute;
    left: 0;
    top: 785px;
    width: 1200px;
    height: 92px;
    margin: 0;
    display: flex;
    align-items: center;
    justify-content: center;
    font-family: "Montserrat", sans-serif;
    font-weight: 500;
    font-size: 42px;
    color: var(--navy);
  }
</style>
</head>
<body>
  <main class="yard-sign">
    <header class="brand">
      <span class="brand-dot" aria-hidden="true"></span>
      <h1 class="brand-name">PL Dunmore Electric</h1>
    </header>
    <section class="slogan-band">
      <p class="slogan">Built on Integrity, Driven by Excellence.</p>
    </section>
    <section class="phone-band">
      <p class="phone">555-214-7796</p>
    </section>
    <div class="rule"></div>
    <p class="website">www.pldunmoreelectric.example</p>
  </main>
</body>
</html>
```